Email Banner Ad for Tidewell Energy company

We are looking for an Email Banner Ad for all emails which is link to website

Regarding MEES compliance coming in April 2018

All the details can be found on our website www.lumenvista.co.uk

Our current footer is attached from last year and we are looking for a new one

Target Market(s)

Property companies and investor

Industry/Entity Type

It Company

Requirements
Must have
• a link to website
• must be the size to go at the bottom of emails
Nice to have
• similar to website
• similar to the advertisement we have had done already

```html
<!DOCTYPE html>
<html lang="en">
<head>
<meta charset="utf-8">
<title>Tidewell Energy – MEES compliance summit banner</title>
<link rel="stylesheet" href="https://fonts.googleapis.com/css2?family=Oswald:wght@500&family=Open+Sans:wght@400;600&display=swap">
<style>
  :root {
    --panel-grey: #8f9092;
    --panel-grey-light: #a9aaac;
    --text-white: #ffffff;
    --grass-dark: #2f6a1c;
    --grass-mid: #4f9a2a;
    --grass-light: #8cc63f;
    --bulb-glow: #e8f26a;
    --icon-white: #ffffff;
  }
  html, body {
    margin: 0;
    padding: 0;
    overflow: hidden;
    background: #ffffff;
  }
  .banner {
    position: relative;
    width: 1200px;
    height: 150px;
    overflow: hidden;
    background: var(--panel-grey);
    font-family: "Open Sans", Arial, sans-serif;
    color: var(--text-white);
  }
  .banner__backdrop {
    position: absolute;
    inset: 0;
  }
  .banner__content {
    position: absolute;
    left: 560px;
    width: 400px;
    top: 0;
    height: 150px;
    text-align: center;
  }
  .banner__title {
    position: absolute;
    top: 28px;
    left: 0;
    right: 0;
    margin: 0;
    font-family: "Oswald", "Arial Narrow", sans-serif;
    font-weight: 500;
    font-size: 33px;
    line-height: 1;
    letter-spacing: 0.2px;
  }
  .banner__venue {
    position: absolute;
    top: 82px;
    left: 0;
    right: 0;
    margin: 0;
    font-size: 18.5px;
    font-weight: 600;
    line-height: 1;
  }
  .banner__footer {
    position: absolute;
    top: 121px;
    left: 647px;
    display: flex;
    align-items: center;
  }
  .banner__link {
    color: var(--text-white);
    text-decoration: none;
    font-size: 12.5px;
    line-height: 18px;
  }
  .banner__social {
    display: flex;
    gap: 22px;
    margin-left: 52px;
  }
  .social-dot {
    width: 19px;
    height: 19px;
    border-radius: 50%;
    background: var(--icon-white);
  }
</style>
</head>
<body>
  <div class="banner">
    <svg class="banner__backdrop" width="1200" height="150" viewBox="0 0 1200 150" aria-hidden="false">
      <defs>
        <linearGradient id="grassTone" x1="0" y1="0" x2="0" y2="1">
          <stop offset="0" stop-color="var(--grass-light)"/>
          <stop offset="0.5" stop-color="var(--grass-mid)"/>
          <stop offset="1" stop-color="var(--grass-dark)"/>
        </linearGradient>
        <radialGradient id="bulbGlow" cx="0.55" cy="0.35" r="0.35">
          <stop offset="0" stop-color="var(--bulb-glow)" stop-opacity="0.85"/>
          <stop offset="1" stop-color="var(--bulb-glow)" stop-opacity="0"/>
        </radialGradient>
        <linearGradient id="networkTone" x1="0" y1="0" x2="1" y2="1">
          <stop offset="0" stop-color="var(--panel-grey)"/>
          <stop offset="1" stop-color="var(--panel-grey-light)"/>
        </linearGradient>
      </defs>
      <g role="img" aria-label="Photo of light bulbs lying on green grass, one bulb lit">
        <polygon points="0,0 576,0 528,150 0,150" fill="url(#grassTone)"/>
        <polygon points="0,0 576,0 528,150 0,150" fill="url(#bulbGlow)"/>
      </g>
      <g role="img" aria-label="Faint geometric network pattern of lines and dots">
        <polygon points="888,0 1200,0 1200,150 1040,150 960,60" fill="url(#networkTone)" opacity="0.7"/>
      </g>
    </svg>

    <div class="banner__content">
      <h1 class="banner__title">MEES compliance summit</h1>
      <p class="banner__venue">The Harrowgate Hall, London | April 2018</p>
    </div>

    <div class="banner__footer">
      <a class="banner__link" href="http://www.lumenvista.co.uk">http://www.lumenvista.co.uk</a>
      <div class="banner__social" aria-label="Social media">
        <span class="social-dot"></span>
        <span class="social-dot"></span>
        <span class="social-dot"></span>
      </div>
    </div>
  </div>
</body>
</html>
```